Apartment Complex in Southeastern US needs new signage & identity!

Need a design for a physical sign/logo & signage for a 28 unit apartment complex in West Columbia, South Carolina, USA.

These are properties that, in their market , I would describe as "affordable." They are no-frills accommodations that are safe, clean and inexpensive.

The sign I want foremost is something that will be free-standing (not attached). Approximate measurements of the main finished sign should be about 4' x 6' (but really this is just an aspect ratio of course.)

Ideally also want to have smaller signs of a coordinated design created to denote the building number (maybe even on each door), but that is a secondary task. You'll get an idea for how ugly the current numbering and signage looks in some of the attached photos. Some of the photos also came from the old Chatterly page of the prior management company. (This project could also possibly expand into creating new assets for taking over and rebranding that chatterly page.)

The apartments are currently called "Brackwell Properties" but frankly speaking I despise this name and want to change (rebrand) it. As the new owner I am thinking to change the name:

Sign should basically say something like the following...

Hollin Apartments
1 & 2 Bedroom Units
3817 Dunmore Creek Rd.
Professionally Managed by
Ferrow Properties: (XXX)XXX-XXXX

"Managed by" part should be detachable. For instance if I ever need to change management companies, I'd just want to be able to swap out that part of the sign, not the whole thing, of course.

Another consideration is that it would be good if there could be a "units available" or "move-in-special" part that could be attached to the top based on the property's status.

I think that earth colors are favorable and nice looking for what this is and where it is located.... greens/browns/tans/greys, etc.

Many similar signs I've seen online and in person have an this Fair Tenancy Pledge logo on it (one of the example signs in the attached images appears this way). I may want to have that appear on the sign -- I'm not yet decided.

I'm attaching some logos of similar signs, as well as some photos of the property itself. You can probably also find more information and photos (Mapvista Road Lens.)

I can answer any question or inquiry you might have in pretty short time.

Target Market(s)

- Low-Mid income singles & families in the Southeast US looking for safe & affordable housing

Industry/Entity Type

Apartment

Requirements
Must have
• - A design proposal for an outdoor sign
• - Design for sign should have some 'detachable' parts for the management company, and to indicate whether units are available and
Nice to have
• - "Earthy" colors: tans/browns/greens etc. seem like it might be nice. (The region, [US postal code 28413] has lots and lots of pine trees.)
Should not have
• No comic sans! :)

```html
<!DOCTYPE html>
<html lang="en">
<head>
<meta charset="utf-8">
<title>Hollin Apartments – Freestanding Sign</title>
<link rel="stylesheet" href="https://fonts.googleapis.com/css2?family=Cinzel:wght@400;700;900&display=swap">
<style>
  :root {
    --brown: #7d3a10;
    --brown-soft: #8c4a1c;
    --tan: #c89a48;
    --tan-light: #e2c27e;
    --cream: #f7f2cf;
    --leaf: #9cbf2e;
    --paper: #ffffff;
  }
  html, body {
    margin: 0;
    padding: 0;
    width: 1200px;
    height: 848px;
    overflow: hidden;
    background: var(--paper);
  }
  .sign {
    display: block;
    width: 1200px;
    height: 848px;
    font-family: "Cinzel", Georgia, serif;
  }
  .post { fill: var(--tan); }
  .frame-outer { fill: var(--brown); }
  .frame-band { fill: var(--tan-light); }
  .face { fill: var(--cream); }
  .face-rule { fill: none; stroke: var(--brown); stroke-width: 2; }
  .hanger { fill: var(--tan); }
  .emblem { fill: var(--leaf); stroke: var(--tan); stroke-width: 4; }
  .emblem-name { fill: var(--brown); font-weight: 700; font-size: 26px; }
  .title { fill: var(--brown); font-weight: 900; font-size: 72px; }
  .subtitle { fill: var(--brown); font-weight: 400; font-size: 24px; }
  .units { fill: var(--brown); font-weight: 700; font-size: 11px; }
  .address { fill: var(--brown); font-weight: 700; font-size: 19px; }
  .divider { stroke: var(--tan); stroke-width: 2.5; }
  .managed { fill: var(--brown-soft); font-weight: 400; font-size: 17px; }
  .manager { fill: var(--brown); font-weight: 700; font-size: 18px; }
</style>
</head>
<body>
<svg class="sign" viewBox="0 0 1200 848" xmlns="http://www.w3.org/2000/svg">
  <!-- posts -->
  <g class="posts">
    <circle class="post" cx="305" cy="193" r="20"/>
    <rect class="post" x="277" y="215" width="56" height="22"/>
    <rect class="post" x="289" y="230" width="31" height="436"/>
    <circle class="post" cx="884" cy="193" r="20"/>
    <rect class="post" x="856" y="215" width="56" height="22"/>
    <rect class="post" x="868" y="230" width="31" height="436"/>
  </g>

  <!-- main panel -->
  <g class="main-panel">
    <rect class="hanger" x="312" y="286" width="16" height="12"/>
    <rect class="hanger" x="312" y="446" width="16" height="12"/>
    <rect class="hanger" x="858" y="286" width="16" height="12"/>
    <rect class="hanger" x="858" y="446" width="16" height="12"/>
    <path class="frame-outer" d="M323,247 H428 C472,247 482,191 593,191 C704,191 714,247 758,247 H863 V494 H323 Z"/>
    <path class="frame-band" d="M331,255 H430 C476,255 486,200 593,200 C700,200 710,255 756,255 H855 V486 H331 Z"/>
    <path class="face" d="M337,261 H432 C478,261 488,207 593,207 C698,207 708,261 754,261 H849 V480 H337 Z"/>
    <path class="face-rule" d="M342,266 H434 C480,266 490,213 593,213 C696,213 706,266 752,266 H844 V475 H342 Z"/>

    <ellipse class="emblem" cx="593" cy="272" rx="75" ry="51" role="img" aria-label="Hollin pine emblem area"/>
    <text class="emblem-name" x="593" y="281" text-anchor="middle">Hollin</text>

    <text class="title" x="593" y="384" text-anchor="middle" textLength="410" lengthAdjust="spacingAndGlyphs">HOLLIN</text>
    <line class="divider" x1="400" y1="405" x2="459" y2="405"/>
    <line class="divider" x1="727" y1="405" x2="786" y2="405"/>
    <text class="subtitle" x="593" y="413" text-anchor="middle" textLength="256" lengthAdjust="spacing">APARTMENTS</text>
    <text class="units" x="593" y="429" text-anchor="middle">1 &amp; 2 Bedroom Units</text>
    <text class="address" x="593" y="461" text-anchor="middle">3817 Dunmore Creek Rd.</text>
  </g>

  <!-- detachable management panel -->
  <g class="manager-panel">
    <rect class="hanger" x="356" y="473" width="8" height="60"/>
    <rect class="hanger" x="822" y="473" width="8" height="60"/>
    <rect class="frame-outer" x="323" y="511" width="540" height="87"/>
    <rect class="frame-band" x="331" y="519" width="524" height="71"/>
    <rect class="face" x="337" y="525" width="512" height="59"/>
    <text class="managed" x="593" y="549" text-anchor="middle">Professionally Managed by</text>
    <text class="manager" x="593" y="575" text-anchor="middle">Ferrow Properties: (XXX)XXX-XXXX</text>
  </g>
</svg>
</body>
</html>
```